Homepage layout for online ad network

Attached is our Calvrex Media logo and updated brief (I can't seem to delete the old logo and brief, but they're no longer relevant).

This project was originally posted with a different logo and corporate name, but we have decided to stay with our current logo and name and redesign the site.

Your design is for a homepage only - design, no coding (I'll get someone else to take your PSD and code it).

Your homepage will make use of a Flash slider - BUT YOU ARE NOT REQUIRED TO PROVIDE THE FLASH. Instead, simply provide the layout and at least two static examples out of the four different sections that will eventually be in the slider.

Much of this design is based on the design of a competitor (listed in the brief).

Please ask whatever questions you need to in order to clarify instructions.
Updates

Project updated to include new logo (and correspondingly new color scheme).

Brief changed slightly.

Thank you for submitting designs for this project in the past.

After some internal strategy work, we have decided to retain our initial corporate identity, Calvrex Media.

If you have submitted a design for the original brief and are available, please re-work your best prior design to reflect the color scheme in the newly uploaded logo.

Target Market(s)

This site is aimed primarily at young professionals who buy digital media on behalf of large advertisers.

Industry/Entity Type

Media

Requirements
Must have
• modern white space
Should not have
• no Flash outside of slider

```html
<!DOCTYPE html>
<html lang="en">
<head>
<meta charset="utf-8">
<title>Calvrex Media — Homepage</title>
<link href="https://fonts.googleapis.com/css2?family=Montserrat:wght@500;600;700&family=Roboto+Condensed:wght@300;400;700&family=Arimo:wght@400;700&display=swap" rel="stylesheet">
<style>
  :root {
    --red: #c41e2e;
    --ink: #1d1b1c;
    --text: #2b2b2b;
    --panel: #f8f8f8;
    --rule: #8a8a8a;
    --lime-light: #f2f655;
    --lime-dark: #c6d22a;
    --slide-bg: #e9ecef;
  }
  * { margin: 0; padding: 0; box-sizing: border-box; }
  html, body { width: 1200px; height: 1000px; overflow: hidden; background: #fff; }
  body { position: relative; font-family: "Arimo", Helvetica, Arial, sans-serif; color: var(--text); }

  .site-header { position: absolute; left: 0; top: 0; width: 1200px; height: 116px; background: #fff; }
  .brand { position: absolute; left: 135px; top: 34px; display: flex; align-items: center; gap: 12px; }
  .brand-mark { width: 26px; height: 26px; background: var(--red); }
  .brand-name { font-family: "Montserrat", sans-serif; font-weight: 600; font-size: 34px; color: var(--ink); letter-spacing: -0.5px; }
  .brand-pointer { position: absolute; left: 253px; top: 101px; width: 0; height: 0; border-left: 8px solid transparent; border-right: 8px solid transparent; border-bottom: 14px solid var(--red); }
  .tagline { position: absolute; right: 119px; top: 26px; font-family: "Montserrat", sans-serif; font-weight: 700; font-size: 11.5px; color: var(--red); letter-spacing: 0.3px; }
  .main-nav { position: absolute; right: 118px; top: 68px; display: flex; height: 33px; }
  .main-nav a { display: flex; align-items: center; padding: 0 14px; font-family: "Montserrat", sans-serif; font-weight: 700; font-size: 12.5px; color: var(--ink); text-decoration: none; border-left: 1px solid #555; }
  .main-nav a:first-child { border-left: none; }
  .main-nav a.current-next { border-left-color: var(--red); }
  .main-nav a:last-child { padding-right: 0; }
  .header-rule { position: absolute; left: 0; top: 116px; width: 1200px; height: 4px; background: var(--red); }
  .stage-fade { position: absolute; left: 0; top: 120px; width: 1200px; height: 220px; background: linear-gradient(#cfcfcf, #fff); }

  .hero-slider { position: absolute; left: 123px; top: 150px; width: 960px; height: 352px; background: linear-gradient(90deg, #b9bdc1 0%, #f5f6f7 30%, var(--slide-bg) 100%); box-shadow: 0 6px 8px rgba(0,0,0,0.45); overflow: hidden; }
  .hero-photo { position: absolute; left: 505px; top: 0; width: 455px; height: 352px; background: radial-gradient(ellipse at 45% 55%, #c89478 0%, #a86e55 30%, #4a2a20 60%, #e7ebf0 85%); }
  .hero-copy { position: absolute; left: 105px; top: 122px; }
  .hero-title { font-family: "Montserrat", sans-serif; font-weight: 700; font-size: 39px; color: var(--red); line-height: 1; }
  .hero-sub { margin-top: 8px; font-family: "Montserrat", sans-serif; font-weight: 500; font-size: 20.5px; color: var(--ink); line-height: 24px; letter-spacing: 0.3px; }
  .slider-arrow { position: absolute; top: 157px; }
  .slider-arrow.prev { left: 20px; }
  .slider-arrow.next { right: 18px; }
  .slider-dots { position: absolute; left: 554px; top: 516px; display: flex; gap: 14px; }
  .slider-dots span { width: 14px; height: 14px; border-radius: 50%; background: var(--ink); }

  .content-panel { position: absolute; left: 118px; top: 658px; width: 960px; height: 247px; background: var(--panel); box-shadow: 0 8px 10px -4px rgba(0,0,0,0.3); }
  .news-divider { position: absolute; left: 728px; top: 558px; width: 2px; height: 330px; background: linear-gradient(#fff, #e2e2e2 40%, #e2e2e2 80%, transparent); }

  .about { position: absolute; left: 122px; top: 555px; width: 580px; }
  .about-heading { display: flex; align-items: center; gap: 12px; font-family: "Roboto Condensed", sans-serif; font-size: 25px; color: var(--ink); }
  .about-heading .mark { width: 22px; height: 22px; background: var(--lime-dark); }
  .about-heading b { font-weight: 700; }
  .about-heading span { font-weight: 300; margin-right: 6px; }
  .about-lead { margin-top: 12px; font-size: 17.5px; line-height: 24px; color: var(--red); }
  .about-body { margin-top: 10px; font-size: 14.2px; line-height: 24px; color: var(--text); }
  .footer-rule { position: absolute; left: 122px; top: 835px; width: 577px; height: 1px; background: var(--rule); }
  .footer-links { position: absolute; left: 120px; top: 854px; display: flex; }
  .footer-links a { display: flex; align-items: center; gap: 5px; font-family: "Montserrat", sans-serif; font-weight: 600; font-size: 13px; color: var(--ink); text-decoration: none; letter-spacing: 0.3px; }
  .footer-links a + a { margin-left: 22px; }
  .footer-links a.wide { margin-left: 38px; }

  .news-tab { position: absolute; left: 730px; top: 558px; width: 238px; height: 39px; background: linear-gradient(90deg, var(--lime-light), var(--lime-dark)); box-shadow: 0 2px 4px rgba(0,0,0,0.35); padding-left: 31px; font-family: "Roboto Condensed", sans-serif; font-size: 24px; line-height: 39px; color: var(--red); }
  .news-list { position: absolute; left: 767px; top: 615px; width: 300px; list-style: none; }
  .news-list li { height: 64px; font-size: 12px; line-height: 16px; color: var(--text); }
  .news-list time { display: block; font-weight: 700; color: var(--red); letter-spacing: 0.3px; }

  .copyright { position: absolute; left: 0; top: 924px; width: 1246px; text-align: center; font-size: 11.5px; color: var(--ink); }
</style>
</head>
<body>
  <header class="site-header">
    <div class="brand"><span class="brand-mark"></span><span class="brand-name">Calvrex Media</span></div>
    <span class="brand-pointer"></span>
    <p class="tagline">COMPANY TAGLINE GOES HERE</p>
    <nav class="main-nav">
      <a href="#">BEAUTY</a>
      <a href="#" class="current-next">COOKING</a>
      <a href="#">PARENTING</a>
      <a href="#">ENTERTAINMENT</a>
      <a href="#">VIDEO</a>
      <a href="#">CPC</a>
    </nav>
  </header>
  <div class="header-rule"></div>
  <div class="stage-fade"></div>

  <section class="hero-slider">
    <div class="hero-photo" role="img" aria-label="Photo of a young woman with dark curly hair decorated with yellow flowers"></div>
    <div class="hero-copy">
      <h2 class="hero-title">BEAUTY</h2>
      <p class="hero-sub">SITE SPECIFIC CAMPAIGNS<br>AT RON PRICES</p>
    </div>
    <svg class="slider-arrow prev" width="30" height="50" viewBox="0 0 30 50"><path d="M26 2 L6 25 L26 48 L18 48 L0 25 L18 2 Z" fill="#1d1b1c"/></svg>
    <svg class="slider-arrow next" width="30" height="50" viewBox="0 0 30 50"><path d="M4 2 L24 25 L4 48 L12 48 L30 25 L12 2 Z" fill="#1d1b1c"/></svg>
  </section>
  <div class="slider-dots"><span></span><span></span><span></span><span></span><span></span></div>

  <div class="content-panel"></div>
  <div class="news-divider"></div>

  <section class="about">
    <h2 class="about-heading"><span class="mark"></span><span>ABOUT</span><b>CALVREX MEDIA</b></h2>
    <p class="about-lead">Lorem ipsum dolor sit amet, consectetur adipiscing elit. Mauris dignissim nulla pharetra risus iaculis at consequat turpis vulputate.</p>
    <p class="about-body">Sed scelerisque magna ut quam scelerisque dictum. Morbi purus quam, sodales id vehicula non, ultricies vitae justo. Vivamus sed augue ut elit dapibus adipiscing vel in elit. Mauris adipiscing, elit a laoreet eleifend, orci lacus condimentum enim, vitae venenatis enim velit ac dolor. Nullam augue mauris, tincidunt et bibendum nec, consequat ut dui. Sed id ante in purus vulputate adipiscing ac non justo. Nulla libero sem, venenatis in fringilla pulvinar, ornare ac diam.</p>
  </section>
  <div class="footer-rule"></div>
  <nav class="footer-links">
    <a href="#">ABOUT US <svg width="12" height="10" viewBox="0 0 12 10"><path d="M1 5 H10 M6 1 L10 5 L6 9" stroke="#c41e2e" stroke-width="2" fill="none"/></svg></a>
    <a href="#">CONTACT US <svg width="12" height="10" viewBox="0 0 12 10"><path d="M1 5 H10 M6 1 L10 5 L6 9" stroke="#c41e2e" stroke-width="2" fill="none"/></svg></a>
    <a href="#" class="wide">MANAGEMENT TEAM <svg width="12" height="10" viewBox="0 0 12 10"><path d="M1 5 H10 M6 1 L10 5 L6 9" stroke="#c41e2e" stroke-width="2" fill="none"/></svg></a>
    <a href="#">NEWS <svg width="12" height="10" viewBox="0 0 12 10"><path d="M1 5 H10 M6 1 L10 5 L6 9" stroke="#c41e2e" stroke-width="2" fill="none"/></svg></a>
    <a href="#">CAREERS <svg width="12" height="10" viewBox="0 0 12 10"><path d="M1 5 H10 M6 1 L10 5 L6 9" stroke="#c41e2e" stroke-width="2" fill="none"/></svg></a>
  </nav>

  <h2 class="news-tab">CALVREX NEWS</h2>
  <ul class="news-list">
    <li><time>JANUARY 15, 2011</time>Calvrex Media unveils new web site design and digital strategy</li>
    <li><time>DECEMBER 22, 2010</time>Calvrex Media featured in Foundersweek.com as one<br>of the fastest grown online ad agencies.</li>
    <li><time>NOVEMBER 15, 2010</time>As RTB Goes Mainstream, Display Services Try To<br>Pull Publishers Along</li>
    <li><time>NOVEMBER 9, 2010</time>Morbi purus quam, sodales id vehicula non, ultricies vitae justo</li>
  </ul>

  <p class="copyright">Copyright 2011 Calvrex Media. All Rights Reserved</p>
</body>
</html>
```